Awards Banquet Invitation

The Millbrook Valley Chamber of Commerce is celebrating it's 65th year at our Annual Awards Banquet (business leader awards). Since we were founded in 1950, we will have a 1950's theme. Dress will be 1950's Formal. I don't want cheesy 1950's. I want Classic feel and fonts from that era. This event is for business professionals so looks from ads in the 50's would be good for inspiration. I would like a look that I can use for the program and event ads. Invitation will include an RSVP insert. Date: February 10, 2015. Time: 6 cocktails, 7 dinner & program, Location: Delwen Oaks Country Club. Dress is 1950's formal

Target Market(s)

Business owners - our members

Industry/Entity Type

Business

• Lasalle, linotype, thirsty

Colors
86cfc6
474747
ffffff
000000

Requirements
Must have
• classic 50's font and old-fashioned feel
Should not have
• sock hop, soda fountain, 50's diner

```html
<!DOCTYPE html>
<html lang="en">
<head>
<meta charset="utf-8">
<title>Annual Awards Banquet Invitation and RSVP Card</title>
<link href="https://fonts.googleapis.com/css2?family=Righteous&family=Poiret+One&display=swap" rel="stylesheet">
<style>
  :root {
    --backdrop: #c3c3c3;
    --blue-light: #4aa3ea;
    --blue-mid: #3b8ddb;
    --blue-deep: #2d7ccd;
    --cream: #f4f0e7;
    --navy: #0f3f6e;
    --white: #ffffff;
    --font-display: "Righteous", sans-serif;
    --font-deco: "Poiret One", sans-serif;
  }
  * { margin: 0; padding: 0; box-sizing: border-box; }
  html, body { width: 1016px; height: 1200px; overflow: hidden; }
  body { background: var(--backdrop); position: relative; }

  .card {
    position: absolute;
    top: 305px;
    width: 440px;
    height: 590px;
    box-shadow: 0 6px 18px rgba(0,0,0,0.25);
  }
  .card--invitation { left: 48px; }
  .card--rsvp { left: 528px; }
  .card__art { position: absolute; inset: 0; width: 440px; height: 590px; display: block; }

  .txt { position: absolute; left: 0; width: 100%; text-align: center; line-height: 1.1; }

  .event-date { top: 22px; font-family: var(--font-display); color: var(--white); font-size: 22px; text-align: left; padding-left: 40px; }
  .event-time { font-family: var(--font-deco); color: var(--navy); font-size: 26px; font-weight: 700; }
  .event-time--cocktails { top: 142px; }
  .event-time--dinner { top: 268px; }
  .event-label { font-family: var(--font-deco); color: var(--navy); font-size: 17px; font-weight: 700; }
  .event-label--cocktails { top: 172px; }
  .event-label--dinner { top: 298px; font-style: italic; }
  .event-title { top: 198px; font-family: var(--font-display); color: var(--navy); font-size: 28px; }
  .event-venue { top: 392px; font-family: var(--font-deco); color: var(--white); font-size: 24px; font-weight: 700; }
  .event-dress { top: 436px; font-family: var(--font-deco); color: var(--navy); font-size: 24px; font-weight: 700; }

  .reply-by { top: 18px; font-family: var(--font-deco); color: var(--white); font-size: 21px; font-weight: 700; }
  .rsvp-heading { top: 180px; font-family: var(--font-display); color: var(--navy); font-size: 66px; letter-spacing: 4px; }

  .reply-field { position: absolute; left: 60px; font-family: var(--font-deco); color: var(--white); font-size: 22px; font-weight: 700; }
  .reply-field--name { top: 408px; }
  .reply-field--guest { top: 444px; }

  .reply-option { position: absolute; left: 60px; display: flex; align-items: center; gap: 16px; font-family: var(--font-deco); color: var(--navy); font-size: 19px; font-weight: 700; font-style: italic; }
  .reply-option--accept { top: 488px; }
  .reply-option--decline { top: 526px; }
  .reply-option__dot { width: 22px; height: 22px; border-radius: 50%; background: var(--cream); flex: none; }
</style>
</head>
<body>

<section class="card card--invitation">
  <svg class="card__art" viewBox="0 0 440 590">
    <rect width="440" height="590" fill="var(--blue-light)"/>
    <polygon role="img" aria-label="Blue damask pattern panel" points="0,75 300,0 440,0 440,230 0,410" fill="var(--blue-deep)"/>
    <polygon points="170,340 440,190 440,370" fill="var(--blue-mid)"/>
    <polygon role="img" aria-label="Blue damask pattern band" points="0,505 440,470 440,590 0,590" fill="var(--blue-deep)"/>
    <path d="M95,150 Q110,120 160,118 L300,110 Q340,108 360,140 L395,200 Q410,230 390,260 L350,300 Q330,325 290,322 L140,335 Q100,338 85,300 L60,240 Q50,210 70,185 Z" fill="var(--cream)"/>
  </svg>
  <p class="txt event-date">Feb 10.2015</p>
  <p class="txt event-time event-time--cocktails">18:00</p>
  <p class="txt event-label event-label--cocktails">Cocktails</p>
  <h1 class="txt event-title">Formal Annual Awards<br>Banquet</h1>
  <p class="txt event-time event-time--dinner">19:00</p>
  <p class="txt event-label event-label--dinner">Dinner &amp; Program</p>
  <p class="txt event-venue">Delwen Oaks Country Club</p>
  <p class="txt event-dress">Dresscode: 1950's formal</p>
</section>

<section class="card card--rsvp">
  <svg class="card__art" viewBox="0 0 440 590">
    <rect width="440" height="590" fill="var(--blue-light)"/>
    <polygon role="img" aria-label="Blue damask pattern panel" points="0,75 300,0 440,0 440,230 0,410" fill="var(--blue-deep)"/>
    <polygon points="170,340 440,190 440,370" fill="var(--blue-mid)"/>
    <polygon role="img" aria-label="Blue damask pattern band" points="0,505 440,470 440,590 0,590" fill="var(--blue-deep)"/>
    <path d="M95,150 Q110,120 160,118 L300,110 Q340,108 360,140 L395,200 Q410,230 390,260 L350,300 Q330,325 290,322 L140,335 Q100,338 85,300 L60,240 Q50,210 70,185 Z" fill="var(--cream)"/>
    <line x1="90" y1="430" x2="400" y2="418" stroke="var(--navy)" stroke-width="1.2"/>
    <line x1="125" y1="466" x2="400" y2="454" stroke="var(--navy)" stroke-width="1.2"/>
  </svg>
  <p class="txt reply-by">Please reply by<br>Jan 10.2015</p>
  <h2 class="txt rsvp-heading">RSPV</h2>
  <p class="reply-field reply-field--name">M</p>
  <p class="reply-field reply-field--guest">Guest</p>
  <p class="reply-option reply-option--accept"><span class="reply-option__dot"></span>accept with pleasure</p>
  <p class="reply-option reply-option--decline"><span class="reply-option__dot"></span>decline with regret</p>
</section>

</body>
</html>
```